Hadley's Labouring Service needs a logo/business cards.

i've just started a new Labouring Business, Called Hadley's Labouring Service, I provide high quality labouring servicing to local Builders and Tradesmen.
I'd like my business cards to reflect the hard work and dedication I put into my business.
I'd like to see Burnt Orange and blacks in the cards and logo.
I want my cards to catch peoples eye as there is A lot of dull business cards in my industry.

Target Market(s)

Builders and other tradesmen

Contact Information for Business Card

Hadley's Labouring Service

Font styles to use
Sans Serif

Colors
f78f20
ffc214
000000
ffffff

Requirements
Must have
• My name : Tom Hadley
• My Number: 0497562083
• Email Address : hadleylabouringservice@examplemail.net
• A Sharp and Professional Design
Nice to have
• A unique design that separates my Cards from others,
• As I try to provide unique service to my clients I'd love my cards/logo to reflect this.

```html
<!DOCTYPE html>
<html lang="en">
<head>
<meta charset="utf-8">
<title>Hadley's Labouring Service – Business Cards</title>
<link rel="stylesheet" href="https://fonts.googleapis.com/css2?family=Exo+2:wght@500;600&family=Open+Sans:wght@400&display=swap">
<style>
  :root {
    --backdrop: #2b2b2b;
    --card: #191919;
    --card-edge: #242424;
    --white: #ffffff;
    --amber: #ffc214;
    --orange: #f78f20;
    --silver: #cfcfcf;
    --text-soft: #e8e8e8;
  }
  * { margin: 0; padding: 0; box-sizing: border-box; }
  html, body {
    width: 1200px; height: 1189px; overflow: hidden;
    background: var(--backdrop);
  }
  .canvas { position: relative; width: 1200px; height: 1189px; }
  .card {
    position: absolute; left: 220px;
    width: 760px; height: 430px;
    background: var(--card);
    border: 1px solid var(--card-edge);
    border-radius: 30px;
    box-shadow: 0 18px 40px rgba(0,0,0,0.45);
  }
  .card--front { top: 110px; }
  .card--back { top: 650px; }

  .wordmark {
    display: flex; align-items: center; gap: 14px;
    font-family: "Exo 2", sans-serif; font-weight: 600;
    white-space: nowrap;
  }
  .wordmark__mark { width: 18px; height: 18px; flex: none; }

  .card--front .wordmark {
    position: absolute; left: 50%; top: 50%;
    transform: translate(-50%, -50%);
    font-size: 36px; color: var(--silver);
  }
  .card--front .wordmark__mark { background: var(--orange); width: 24px; height: 24px; }

  .card--back .wordmark {
    position: absolute; left: 40px; top: 196px;
    font-size: 22px; color: var(--white); gap: 10px;
  }
  .card--back .wordmark__mark { background: var(--amber); width: 16px; height: 16px; }

  .divider {
    position: absolute; left: 376px; top: 110px;
    width: 1px; height: 200px; background: var(--amber);
  }
  .contact { position: absolute; left: 404px; top: 118px; right: 18px; }
  .contact__name {
    font-family: "Exo 2", sans-serif; font-weight: 600;
    font-size: 28px; color: var(--white); letter-spacing: 0.5px;
  }
  .contact__role {
    font-family: "Open Sans", sans-serif; font-size: 17px;
    color: var(--amber); margin-top: 2px;
  }
  .contact__list { list-style: none; margin-top: 38px; }
  .contact__item {
    display: flex; align-items: center; gap: 12px;
    font-family: "Open Sans", sans-serif; font-size: 15px;
    color: var(--text-soft); margin-bottom: 10px; white-space: nowrap;
  }
  .contact__icon { width: 18px; height: 18px; flex: none; }
</style>
</head>
<body>
<main class="canvas">
  <section class="card card--front" aria-label="Card front">
    <div class="wordmark">
      <span class="wordmark__mark"></span>
      <span class="wordmark__name">Hadley's Labouring Service</span>
    </div>
  </section>

  <section class="card card--back" aria-label="Card back">
    <div class="wordmark">
      <span class="wordmark__mark"></span>
      <span class="wordmark__name">Hadley's Labouring Service</span>
    </div>
    <div class="divider"></div>
    <div class="contact">
      <p class="contact__name">Tom Hadley</p>
      <p class="contact__role">Manager</p>
      <ul class="contact__list">
        <li class="contact__item">
          <svg class="contact__icon" viewBox="0 0 18 18" aria-hidden="true">
            <rect x="4.5" y="1.5" width="9" height="15" rx="1.5" fill="none" stroke="#ffc214" stroke-width="1.6"/>
            <line x1="8" y1="13.5" x2="10" y2="13.5" stroke="#ffc214" stroke-width="1.6"/>
          </svg>
          <span>0497562083</span>
        </li>
        <li class="contact__item">
          <svg class="contact__icon" viewBox="0 0 18 18" aria-hidden="true">
            <rect x="1" y="3.5" width="16" height="11" fill="#ffc214"/>
            <polyline points="1,3.5 9,10 17,3.5" fill="none" stroke="#191919" stroke-width="1.4"/>
            <line x1="1" y1="14.5" x2="7" y2="9" stroke="#191919" stroke-width="1.2"/>
            <line x1="17" y1="14.5" x2="11" y2="9" stroke="#191919" stroke-width="1.2"/>
          </svg>
          <span>hadleylabouringservice@examplemail.net</span>
        </li>
      </ul>
    </div>
  </section>
</main>
</body>
</html>
```